Business Card Design

Very plain simple card, Plain modern font. Background. Grey fading to black. Large Bright lime green text. Saying.

TWR-ZA.COM

Small other details in white text.

Irish Horse Sales . Livery . Stud . Shows

Mark Dabrowski
TWR
Birch Lodge
Carrowmede Lane
Thistlecombe
Lincolnshire
LN4 7JX

Email. Twrzap@mailvale.co.uk
Tel. 07482 936504

Industry/Entity Type

Business

Contact Information for Business Card

As below

```html
<!DOCTYPE html>
<html lang="en">
<head>
<meta charset="utf-8">
<title>TWR-ZA.COM Business Card</title>
<link rel="stylesheet" href="https://fonts.googleapis.com/css2?family=Barlow:wght@400;500;700&display=swap">
<style>
  :root {
    --page-bg: #e6e6e4;
    --card-grey: #3a3a3a;
    --card-black: #0d0d0d;
    --lime: #7ac943;
    --text-light: #e8e8e8;
    --icon-ink: #1a1a1a;
  }
  * { box-sizing: border-box; margin: 0; padding: 0; }
  html, body {
    width: 1200px;
    height: 873px;
    overflow: hidden;
    background: var(--page-bg);
  }
  .stage {
    width: 1200px;
    height: 873px;
    display: flex;
    align-items: center;
    justify-content: center;
  }
  .business-card {
    position: relative;
    width: 1000px;
    height: 571px;
    background: linear-gradient(135deg, var(--card-grey) 0%, #1f1f1f 45%, var(--card-black) 100%);
    box-shadow: 0 10px 30px rgba(0,0,0,0.25);
    font-family: "Barlow", Arial, sans-serif;
    color: var(--text-light);
    padding: 38px 50px;
  }
  .brand-name {
    font-weight: 700;
    font-size: 150px;
    line-height: 1;
    color: var(--lime);
    letter-spacing: 1px;
    white-space: nowrap;
  }
  .services {
    margin-top: 8px;
    font-size: 27px;
    font-weight: 400;
    letter-spacing: 0.3px;
  }
  .services .dot { color: var(--lime); padding: 0 6px; }
  .contact-name {
    margin-top: 26px;
    font-size: 27px;
    font-weight: 500;
    color: var(--lime);
  }
  .address {
    font-style: normal;
    font-size: 22px;
    line-height: 1.35;
    margin-top: 4px;
  }
  .contact-line {
    display: flex;
    align-items: center;
    gap: 10px;
    font-size: 22px;
    line-height: 1.35;
    margin-top: 2px;
  }
  .contact-line:first-of-type { margin-top: 4px; }
  .icon-badge {
    display: inline-flex;
    align-items: center;
    justify-content: center;
    width: 20px;
    height: 20px;
    background: var(--lime);
    color: var(--icon-ink);
    font-size: 16px;
    font-weight: 700;
    line-height: 1;
  }
</style>
</head>
<body>
  <main class="stage">
    <section class="business-card">
      <h1 class="brand-name">TWR-ZA.COM</h1>
      <p class="services">Irish Horse Sales<span class="dot">•</span>Livery<span class="dot">•</span>Stud<span class="dot">•</span>Shows</p>
      <p class="contact-name">Mark Dabrowski - TWR</p>
      <address class="address">
        Birch Lodge, Carrowmede Lane<br>
        Thistlecombe, Lincolnshire, LN4 7JX
      </address>
      <p class="contact-line"><span class="icon-badge">e</span>Twrzap@mailvale.co.uk</p>
      <p class="contact-line"><span class="icon-badge">t</span>07482 936504</p>
    </section>
  </main>
</body>
</html>
```